Website design for SaaS -solution

We are B2B SaaS company. (Korlet.io) Our software brings leads by enriching company profiles with external data. We want to take load off from marketing and sales directors by bringing them sales leads.

Our core values that we want to communicate:
-Data driven
-Easy going and easy to use
-Sincere and honest
-Humble
-lively

We would like to see designs that obey our colours (logos attached) but also the website should be lively and visual / photo intensive. We only use few sentences to power our message. Here are few examples:

http://www.plovista.com/
https://www.zundel.com/

We will also make a video that we post in the front cover. Our current website is www.korlet.io. The font we would like to use is Avenir Next or similar

• Avenir Next

0455a3
ec1f27
9bcb3c
85acd3

• 1 page: the main page (attached is brief) (This is most important one)
• 2. page: , a design where we can post content such as slides, e-papers etc (e.g.. http://www.brightmoor.com/eu/industries/)
• 3. page: a basic template that can be used for various needs ( team-page, jobs, page, etc)

```html
<!DOCTYPE html>
<html lang="en">
<head>
<meta charset="utf-8">
<title>Korlet – Home</title>
<link rel="stylesheet" href="https://fonts.googleapis.com/css2?family=Arimo:wght@400;700&family=Nunito+Sans:wght@400;600;700&family=Roboto+Condensed:wght@300;400&family=Source+Sans+3:wght@600;700&display=swap">
<style>
:root{
  --brand:#0455a3;
  --brand-deep:#0a4c95;
  --brand-soft:#85acd3;
  --topbar:#333333;
  --ink:#222222;
  --body:#444444;
  --band:#e6e6e6;
  --card:#e6e6e6;
  --footer:#141414;
  --footer-base:#0a0a0a;
  --footer-head:#2a6fc0;
  --white:#ffffff;
}
*{box-sizing:border-box;margin:0;padding:0}
html,body{width:706px;height:1200px;overflow:hidden;background:var(--white)}
body{position:relative;font-family:"Arimo",Arial,sans-serif;color:var(--body)}
.abs{position:absolute}

/* top bar */
.topbar{left:0;top:0;width:706px;height:26px;background:var(--topbar)}
.social-mini{left:60px;top:6px;display:flex;gap:4px}
.social-mini span{width:15px;height:14px;display:block}
.utility{right:78px;top:0;height:26px;display:flex;align-items:center;font-size:8.5px;color:var(--white);gap:9px}
.utility .sep{opacity:.8}

/* header */
.brand{left:60px;top:48px;display:flex;align-items:center;gap:10px}
.brand-dot{width:28px;height:28px;border-radius:50%;background:var(--brand)}
.brand-name{font-family:"Nunito Sans",sans-serif;font-weight:400;font-size:30px;color:#9a9a9a;letter-spacing:.5px}
.mainnav{left:322px;top:74px;display:flex;font-family:"Nunito Sans",sans-serif;font-size:8.5px;font-weight:600;color:var(--ink)}
.mainnav a{color:inherit;text-decoration:none;height:19px;line-height:19px;padding:0 9px;margin-right:12px}
.mainnav a.active{background:var(--brand);color:var(--white);margin-right:13px}

/* hero */
.hero-media{left:0;top:98px;width:706px;height:295px;background:linear-gradient(100deg,#c9d2da 0%,#e9eef2 35%,#cdd8e2 60%,#aebfce 100%)}
.hero-panel{left:461px;top:110px;width:218px;height:270px;background:rgba(4,85,163,.85);border:1px solid #2d4f78}
.hero-panel h2{font-family:"Nunito Sans",sans-serif;font-weight:600;font-size:15px;color:var(--white);position:absolute;left:17px;top:14px}
.hero-panel p{font-size:8.6px;line-height:13px;color:var(--white);position:absolute}
.intro-copy{left:17px;top:37px;width:188px;text-align:justify}
.btn-dark{position:absolute;left:138px;top:104px;width:60px;height:22px;background:#111;border:1px solid #ddd;color:var(--white);font-size:8.5px;display:flex;align-items:center;justify-content:center}
.engage{position:absolute;left:9px;top:138px;width:199px;height:98px;background:#0f2a4c}
.engage h3{font-family:"Nunito Sans",sans-serif;font-weight:600;font-size:14px;color:var(--white);position:absolute;left:9px;top:6px}
.engage p{left:10px;top:34px;width:182px;line-height:14px}
.engage .link{position:absolute;right:10px;bottom:8px;font-size:8.5px;color:var(--white);text-decoration:underline}

/* signup band */
.signup{left:0;top:393px;width:706px;height:48px;background:var(--band)}
.signup-input{position:absolute;left:203px;top:12px;width:229px;height:25px;background:var(--white);border:1px solid #d6d6d6;font-size:8px;color:#888;padding-left:10px;line-height:23px}
.signup-btn{position:absolute;left:437px;top:12px;width:59px;height:25px;background:var(--brand);color:var(--white);font-family:"Nunito Sans",sans-serif;font-size:11px;font-weight:600;display:flex;align-items:center;justify-content:center}

/* intro */
.section-title{left:0;width:706px;text-align:center;font-family:"Nunito Sans",sans-serif;font-weight:400;color:var(--ink)}
.intro-title{top:458px;font-size:19px}
.intro-sub{left:0;top:490px;width:706px;text-align:center;font-size:8.6px;color:#444}

/* service cards */
.card{top:566px;width:187px;height:147px;background:var(--card)}
.card-icon{position:absolute;width:88px;height:88px}
.card h4{position:absolute;left:0;top:56px;width:100%;text-align:center;font-family:"Roboto Condensed",sans-serif;font-weight:300;font-size:18px;color:var(--ink);letter-spacing:.3px}
.card p{position:absolute;left:10px;top:82px;width:167px;text-align:center;font-size:8.5px;line-height:11.6px;color:#444}

/* testimonials */
.testimonials{left:0;top:738px;width:706px;height:235px;background:linear-gradient(135deg,#0b4fa6 0%,#1a63bf 45%,#0f58b0 70%,#0a4a9c 100%)}
.testimonials h2{top:19px;color:var(--white);font-size:18px}
.avatar{position:absolute;left:320px;top:59px;width:50px;height:50px;border-radius:50%;border:2px solid var(--white);background:linear-gradient(160deg,#9a7a6a,#d8c0b0)}
.quote{position:absolute;left:50px;top:122px;width:606px;text-align:center;font-family:"Source Sans 3",sans-serif;font-weight:600;font-size:9.5px;line-height:14.3px;color:var(--white)}
.byline{position:absolute;left:0;width:706px;text-align:center;font-family:"Source Sans 3",sans-serif;font-weight:700;font-size:8.8px;color:var(--white)}

/* footer */
.footer{left:0;top:973px;width:706px;height:192px;background:var(--footer)}
.footer h5{position:absolute;top:23px;font-family:"Nunito Sans",sans-serif;font-weight:600;font-size:10.5px;color:var(--footer-head)}
.contact-item{position:absolute;left:60px;display:flex;align-items:flex-start;gap:8px;font-size:7.8px;color:var(--white);line-height:10px}
.contact-item svg{flex:none}
.tweet{position:absolute;left:219px;width:120px;font-size:6.8px;line-height:8.3px;color:#bdbdbd}
.tweet b{color:#e4e4e4;font-size:7.4px}
.tweet .handle{color:#8a8a8a}
.tweet .url{color:#4a8fdc}
.about-links{position:absolute;left:368px;top:51px;font-size:7.6px;color:var(--white);line-height:17.6px;list-style:none}
.follow-copy{position:absolute;left:512px;top:51px;width:137px;font-size:7.6px;line-height:11.6px;color:var(--white);text-align:justify}
.follow-icons{position:absolute;left:513px;top:115px;display:flex;gap:5px}
.follow-icons span{width:18px;height:18px;background:#555;display:block}
.footer-brand{position:absolute;left:536px;top:153px;display:flex;align-items:center;gap:7px}
.footer-brand i{width:16px;height:16px;border-radius:50%;background:#555;display:block}
.footer-brand span{font-family:"Nunito Sans",sans-serif;font-size:18px;color:#555}
.base{left:0;top:1165px;width:706px;height:35px;background:var(--footer-base);font-size:8.2px;color:var(--white)}
.base .copy{position:absolute;left:59px;top:12px}
.base .legal{position:absolute;right:58px;top:12px}
</style>
</head>
<body>

<header>
  <div class="abs topbar">
    <div class="abs social-mini" aria-label="Social channels">
      <span style="background:#2aa6e0"></span><span style="background:#f59a22"></span><span style="background:#3b5a9a"></span><span style="background:#d8262a"></span><span style="background:#2f2f2f"></span><span style="background:#1c86c6"></span>
    </div>
    <nav class="abs utility">
      <span>Login</span><span class="sep">|</span><span>Blog</span><span class="sep">|</span><span>Contact</span><span class="sep">|</span><span>+1.800.555.0148</span><span class="sep">|</span><span>Americas (English)</span>
    </nav>
  </div>

  <div class="abs brand"><i class="brand-dot"></i><span class="brand-name">korlet</span></div>
  <nav class="abs mainnav">
    <a class="active">HOME</a><a>TEAM</a><a>PRODUCTS</a><a>CUSTOMER</a><a>CAREERS</a>
  </nav>
</header>

<section>
  <div class="abs hero-media" role="img" aria-label="Photo of two businessmen in white shirts reviewing a tablet in a bright office"></div>
  <div class="abs hero-panel">
    <h2>What Korlet is</h2>
    <p class="intro-copy">We go through open data and identify with prospective purchase behavior signals. We gather every day a huge amount of information that organizations focus our right and we value their sales potential perspective.</p>
    <span class="btn-dark">Learn More</span>
    <div class="engage">
      <h3>Engage Everywhere</h3>
      <p>We go through open data and identify with prospective purchase behavior signals. We gather every day a huge amount</p>
      <span class="link">Learn More</span>
    </div>
  </div>
</section>

<section class="abs signup">
  <div class="signup-input">Enter Your Business Mail</div>
  <div class="signup-btn">Submit</div>
</section>

<section>
  <h1 class="abs section-title intro-title">Is B2B sales completely gone digital?</h1>
  <p class="abs intro-sub">Lorem Ipsum is simply dummy text of the printing and typesetting industry Ipsum has been the industry's standard dummy text</p>

  <article class="abs card" style="left:59px">
    <svg class="card-icon" style="left:50px;top:-41px" viewBox="0 0 88 88"><circle cx="44" cy="44" r="42" fill="#0a4c95"/><circle cx="41" cy="45" r="36" fill="#fff"/></svg>
    <h4>MARKETING</h4>
    <p>We go through open data and identify with prospective purchase behavior signals. We gather every day a huge amount of information that organizations</p>
  </article>
  <article class="abs card" style="left:260px">
    <svg class="card-icon" style="left:50px;top:-41px" viewBox="0 0 88 88"><circle cx="44" cy="44" r="42" fill="#0a4c95"/><circle cx="41" cy="45" r="36" fill="#fff"/></svg>
    <h4>SALES</h4>
    <p>We go through open data and identify with prospective purchase behavior signals. We gather every day a huge amount of information that organizations</p>
  </article>
  <article class="abs card" style="left:461px">
    <svg class="card-icon" style="left:50px;top:-41px" viewBox="0 0 88 88"><circle cx="44" cy="44" r="42" fill="#0a4c95"/><circle cx="41" cy="45" r="36" fill="#fff"/></svg>
    <h4>INDUSTRY EXPERT</h4>
    <p>We go through open data and identify with prospective purchase behavior signals. We gather every day a huge amount of information that organizations</p>
  </article>
</section>

<section class="abs testimonials">
  <h2 class="abs section-title">Our Testimonials</h2>
  <div class="avatar" role="img" aria-label="Portrait photo of the client giving the testimonial"></div>
  <p class="quote">"Korlet help us to find new potential customers and also to deepen existing customer relationships. Scent desire to customize exactly to our needs service tool has been ihaltavaa "Korlet help us to find new potential customers and also to deepen existing customer relationships. Scent desire to customize exactly to our needs service tool has been ihaltavaa""</p>
  <p class="byline" style="top:179px">Written By</p>
  <p class="byline" style="top:194px">AARNE LINDQVIST, SALES MANAGER, TORVANE LTD</p>
</section>

<footer>
  <div class="abs footer">
    <h5 style="left:60px">Contact us</h5>
    <div class="contact-item" style="top:52px">
      <svg width="12" height="12" viewBox="0 0 12 12"><circle cx="6" cy="6" r="5.3" fill="none" stroke="#2a6fc0" stroke-width="1.2"/><path d="M4 3.3l1 1.4-.6.7c.4.9 1 1.5 1.9 1.9l.7-.6 1.4 1-.6 1C5.7 8.5 3.5 6.3 3.3 4z" fill="#2a6fc0"/></svg>
      <span>03 5550 0187 (Phone)</span>
    </div>
    <div class="contact-item" style="top:81px">
      <svg width="12" height="12" viewBox="0 0 12 12"><path d="M1 4c2-2.5 8-2.5 10 0l-1.5 1.3-1.6-1v-1c-1.2-.4-2.6-.4-3.8 0v1l-1.6 1z" fill="#2a6fc0"/><rect x="2.5" y="6" width="7" height="4.5" rx="1" fill="#2a6fc0"/></svg>
      <span>03 5550 0187 (Fax)</span>
    </div>
    <div class="contact-item" style="top:110px">
      <svg width="12" height="12" viewBox="0 0 12 12"><rect x="1" y="2.5" width="10" height="7" fill="#2a6fc0"/><path d="M1 2.5l5 4 5-4" fill="none" stroke="#141414" stroke-width="1"/></svg>
      <span>hello@korlet.example</span>
    </div>
    <div class="contact-item" style="top:139px">
      <svg width="12" height="12" viewBox="0 0 12 12"><path d="M6 11.5S2 7 2 4.5a4 4 0 0 1 8 0C10 7 6 11.5 6 11.5z" fill="#2a6fc0"/><circle cx="6" cy="4.5" r="1.5" fill="#141414"/></svg>
      <span>PO Box : 4120, Harbour Lorem<br>ipsum dollor si2210</span>
    </div>

    <h5 style="left:217px">Social Feed</h5>
    <p class="tweet" style="top:52px"><b>Saima</b> <span class="handle">@quillnote</span><br>How to Download Photos from Pinl task to take photos from Pinly bu to... <span class="url">pinly.co/Q4rtLm8vWa</span></p>
    <p class="tweet" style="top:97px"><b>Saima</b> <span class="handle">@quillnote</span><br>How to Download Photos from Pinl task to take photos from Pinly bu to... <span class="url">pinly.co/Q4rtLm8vWa</span></p>
    <p class="tweet" style="top:142px"><b>Saima</b> <span class="handle">@quillnote</span><br>How to Download Photos from Pinl task to take photos from Pinly bu to... <span class="url">pinly.co/Q4rtLm8vWa</span></p>

    <h5 style="left:368px">About Us</h5>
    <ul class="about-links">
      <li>Investor</li><li>Careers</li><li>Terms &amp; Conditions of Services</li><li>Privacy Policy</li><li>Services Level Agreement</li><li>Master Commerical Agfrement</li>
    </ul>

    <h5 style="left:510px">Follow Us</h5>
    <p class="follow-copy">Lorem Ipsum is simply dummy text of the printing and typesetting industry. Lorem Ipsum has been the industry's standard dummy text ever since the 1500s,</p>
    <div class="follow-icons" aria-label="Social channels"><span></span><span></span><span></span><span></span><span></span><span></span></div>
    <div class="footer-brand"><i></i><span>korlet</span></div>
  </div>

  <div class="abs base">
    <span class="copy">© Copyright 2015, Plovista, Inc. All rights reserved.</span>
    <span class="legal">Site Map | Legal | Privacy | Cookies</span>
  </div>
</footer>

</body>
</html>
```